K.M. Bookkeeping Services Resumé

I am looking for a new design/look for a business resume. I have attached an example of another person's resume that gave me the inspiration to revamp our business resume. I am looking for something simple, fresh, not trendy, timeless, and at the same time innovative. I have attached the business card design, the resume, and the example of the resume that caught our eye. If you have any questions please feel free to ask.

```html
<!DOCTYPE html>
<html lang="en">
<head>
<meta charset="utf-8">
<title>K.M. Bookkeeping Services – Resumé</title>
<link href="https://fonts.googleapis.com/css2?family=Roboto:wght@300;400&family=Roboto+Condensed:wght@300;400&display=swap" rel="stylesheet">
<style>
  :root {
    --bg-teal: #5f9b9e;
    --panel: #e6dab9;
    --ink: #4a463e;
    --navy-teal: #2e5a6c;
    --maroon: #8a2a3c;
    --mint: #80c0b6;
    --rule-teal: #2e5a6c;
  }
  * { margin: 0; padding: 0; box-sizing: border-box; }
  html, body { width: 849px; height: 1200px; overflow: hidden; }
  body {
    position: relative;
    background: var(--bg-teal);
    font-family: "Roboto Condensed", "Arial Narrow", sans-serif;
    font-weight: 300;
    color: var(--ink);
  }
  .panel {
    position: absolute;
    left: 33px; width: 782px;
    background: var(--panel);
    border-radius: 22px;
  }
  .panel--profile { top: 127px; height: 380px; }
  .panel--experience { top: 567px; height: 556px; }

  .badge {
    position: absolute;
    left: 67px; width: 66px; height: 66px;
    border-radius: 14px;
    display: flex; align-items: center; justify-content: center;
  }
  .badge--info { top: 86px; background: var(--navy-teal); }
  .badge--gears { top: 528px; background: var(--maroon); }

  .brand-tile {
    position: absolute;
    left: 676px; top: 42px; width: 108px; height: 108px;
    background: var(--mint);
    border: 2px solid #d9ece8;
    border-radius: 20px;
    display: flex; align-items: center; justify-content: center;
    text-align: center;
    padding: 10px;
    font-size: 15px; font-weight: 400; line-height: 1.15;
    color: #23312f;
  }

  .section-title {
    position: absolute;
    left: 62px; width: 728px;
    font-family: "Roboto", Arial, sans-serif;
    font-weight: 300;
    font-size: 26.5px;
    letter-spacing: -0.6px;
    line-height: 1;
    padding-bottom: 9px;
    border-bottom: 1px solid var(--rule-teal);
    color: var(--navy-teal);
  }
  .section-title--role { top: 171px; }
  .section-title--software { top: 390px; border-bottom: none; left: 68px; }
  .section-title--experience { top: 618px; color: var(--maroon); border-bottom-color: var(--maroon); }

  .summary {
    position: absolute;
    left: 64px; top: 220px; width: 712px;
    font-size: 12.6px; line-height: 17px;
  }

  .bullet-grid {
    position: absolute;
    left: 75px;
    list-style: none;
    display: grid;
    grid-template-columns: 133px 143px 133px 140px;
    grid-auto-flow: column;
    grid-template-rows: repeat(3, 17px);
    font-size: 12.6px; line-height: 17px;
  }
  .bullet-grid li::before { content: "• "; }
  .bullet-grid--skills { top: 314px; }
  .bullet-grid--software { top: 425px; }

  .role-heading {
    position: absolute;
    left: 63px; top: 669px;
    font-family: "Roboto", Arial, sans-serif;
    font-size: 20px; font-weight: 300; letter-spacing: -0.6px;
    color: var(--maroon);
  }

  .duties {
    position: absolute;
    left: 64px; top: 702px; width: 705px;
    list-style: none;
    font-size: 12.6px; line-height: 16.4px;
  }
  .duties li { position: relative; padding-left: 13px; }
  .duties li::before {
    content: "-";
    position: absolute; left: 0; top: 0;
    color: var(--maroon); font-weight: 400;
  }

  .contact-bar {
    position: absolute;
    left: 33px; top: 1141px; width: 782px; height: 40px;
    background: var(--mint);
    border-radius: 20px;
    display: flex; align-items: center; justify-content: center;
    color: #ffffff;
    font-size: 15px; font-weight: 400; letter-spacing: -0.2px;
  }
</style>
</head>
<body>

  <div class="panel panel--profile"></div>
  <div class="panel panel--experience"></div>

  <div class="badge badge--info" aria-hidden="true">
    <svg width="30" height="46" viewBox="0 0 30 46">
      <circle cx="15" cy="6" r="5.5" fill="#ffffff"/>
      <path d="M6 16 H20 V38 H25 V45 H5 V38 H10 V23 H6 Z" fill="#ffffff"/>
    </svg>
  </div>

  <div class="brand-tile">K.M. Bookkeeping Services</div>

  <h1 class="section-title section-title--role">ACCOUNTING MANAGER | CONTROLLER</h1>

  <p class="summary">Analytical Accounting Executive with demonstrated expertise in corporate finance management, reporting, forecasting, audits, tax preparation, and state and federal funding.&nbsp; Solid reputation as an expert problem solver who can resolve cross-functional business problems and develop productivity improvement initiatives resulting in increased profitability. Background includes proven success overseeing accounting and finance functions for healthcare organizations, higher education institutions, public and private schools, wholesalers, consulting firms, and logistics companies. Core competencies include:</p>

  <ul class="bullet-grid bullet-grid--skills">
    <li>Profit and Loss</li>
    <li>Financial Reporting</li>
    <li>Audit/Compliance</li>
    <li>Business Analysis</li>
    <li>Systems Automation</li>
    <li>Efficiency Improvement</li>
    <li>Risk Management</li>
    <li>Financial Analysis</li>
    <li>Team Development</li>
    <li>Human Resources</li>
    <li>Modeling/Forecasting</li>
    <li>Expense/Cost Control</li>
  </ul>

  <h2 class="section-title section-title--software">SOFTWARE PROGRAMS</h2>

  <ul class="bullet-grid bullet-grid--software">
    <li>Salarune</li>
    <li>Brimwage</li>
    <li>Marlowfen Systems</li>
    <li>Orvane</li>
    <li>Norvik 7</li>
    <li>Gildmere Suite</li>
    <li>Ledgerloft</li>
    <li>Hollowmere</li>
    <li>Tessary</li>
    <li>Tallyfern</li>
    <li>Penwick</li>
  </ul>

  <div class="badge badge--gears" aria-hidden="true">
    <svg width="50" height="50" viewBox="0 0 50 50" fill="none" stroke="#ffffff" stroke-width="3">
      <circle cx="17" cy="15" r="7"/>
      <circle cx="17" cy="15" r="2.5"/>
      <circle cx="36" cy="27" r="8"/>
      <circle cx="36" cy="27" r="3"/>
      <circle cx="16" cy="37" r="7"/>
      <circle cx="16" cy="37" r="2.5"/>
      <g stroke-linecap="round">
        <path d="M17 5v2M17 23v2M7 15h2M25 15h2M10 8l1.5 1.5M24 8l-1.5 1.5M10 22l1.5-1.5"/>
        <path d="M36 16v2M36 36v2M25 27h2M45 27h2M28 19l1.5 1.5M44 19l-1.5 1.5M44 35l-1.5-1.5M28 35l1.5-1.5"/>
        <path d="M16 27v2M16 45v2M6 37h2M24 37h2M9 30l1.5 1.5M9 44l1.5-1.5M23 44l-1.5-1.5"/>
      </g>
    </svg>
  </div>

  <h2 class="section-title section-title--experience">PROFESSIONAL EXPERIENCE</h2>

  <h3 class="role-heading">K.M.Bookkeeping Services: 2013- Current</h3>

  <ul class="duties">
    <li>Prepare financial statements for medical clinics and various businesses, also billing and payroll, A/P, A/R, internal controls and other systems to comply with regulations. Use Ledgerloft Software for accounting package. Use Gridwell sheets also.</li>
    <li>Working with salons, restaurants, healthcare, small businesses to produce financials, payroll, etc.</li>
    <li>In charge of general ledger and Bank reconciliations and general ledger reconciliations for multiple companies.</li>
    <li>Coordinate and perform intercompany reconciliations. Produce budgets and verify variances as requested by client.</li>
    <li>Work with billing departments to improve A/R aging and billing accuracy.</li>
    <li>Oversee and implement all payroll activities for various businesses. Prepare and file all required state and federal reports, quarterly state unemployment reports, 941's, 940's, W-2's, and 1099's.</li>
    <li>Ability to drive process improvement through the use of technology. Strong ability to manage multiple projects and drive them to timely completion.</li>
    <li>Collaborate with senior management to establish and implement cost containment programs that effectively lower costs and promote employee awareness of cost containment methods.</li>
    <li>Work with accounting auditors and any federal/state agencies to coordinate and complete any required audits.</li>
    <li>Manage credentialing process with various payers; negotiate terms and execute contracts with payers and providers</li>
    <li>Responsible for all Month End closing procedures, related reports and analyses for various business agencies including various analysis of actual performance compared to prior year for Department management, Administrators and Directors.</li>
    <li>Responsible for training staff in accountant duties and monitor staff productivity on an ongoing manner.</li>
    <li>Coordinate Quarterly, Annual reporting requirements with various departments and outside clients.</li>
    <li>Perform revenue and expense analysis as requested by Board of Directors or management.</li>
    <li>Responsible for preparation of the annual operating budget and upload into Ledgerloft Accounting software.</li>
    <li>Provide comparative analysis of actual results vs. forecast throughout the year.</li>
    <li>Perform uploads/imports into the General Ledger system.</li>
    <li>Work as a Revenue Cycle Manager as requested.</li>
    <li>Convert Payroll or accounting processes to computerized system using Tallyfern, Hollowmere, Ledgerloft and other&nbsp; packages.</li>
  </ul>

  <footer class="contact-bar">KATE MORROW&nbsp;|&nbsp;P: 615.555.0142 - E: km@kmbkservices.com - Riverton, TN</footer>

</body>
</html>
```